Local Finance and Insurance Advising Company from Switzerland needs an impressive banner design.

I am looking for an impressive Banner Design, I need this Banner for Facebook, LinkedIn, YouTube & Google.

I am Advising all kind of peoples who are living here in Switzerland. Young, middle age and old people. People who want to go study, people who are planning to create a family, old people who are, or going to retire. Expatriates who want to leave Switzerland to live in another country, expatriates who are coming to Switzerland. Peoples who ant to build their own business up. All kind of financial, insurance and pension planning's.

The Company Name is: Alpine Counsel
Our slogen / heading is: Clear Guidance, no Pitch

The Company logo can be used for the banner, but I would preffer to have the banner without logo, as the logo will be already in a another field on the social networks.

Since the first impression is the most important, this project is really important to me. I am ready to realize further projects with the one who can create the perfect banner who hits the point as described. I am a start-up company, everything is still on beginning and still much has to be done.

Target Market(s)

private clients

Requirements
Must have
• The banner should give the impression of happiness, safeness, health and freedom. Empowering people and creating freedom lifestyles.
Should not have
• I do not want that the banner looks like we are some kind of broker who is just selling some kind of insurances.

```html
<!DOCTYPE html>
<html lang="en">
<head>
<meta charset="utf-8">
<title>Alpine Counsel — Clear Guidance, no Pitch</title>
<link rel="stylesheet" href="https://fonts.googleapis.com/css2?family=Montserrat:wght@500;700&display=swap">
<style>
  :root {
    --brand-red: #d8171e;
    --text-grey: #6b6b6b;
    --paper: #ffffff;
    --mist-light: #f6f6f6;
    --mist-dark: #e4e4e4;
    --photo-warm: #b59a82;
    --photo-deep: #4a4f63;
  }
  html, body {
    margin: 0;
    padding: 0;
    overflow: hidden;
    background: var(--paper);
  }
  .banner {
    position: relative;
    width: 1200px;
    height: 457px;
    overflow: hidden;
    background: var(--paper);
    font-family: "Montserrat", Arial, sans-serif;
  }
  .banner__shapes {
    position: absolute;
    inset: 0;
    width: 1200px;
    height: 457px;
  }
  .brand-name {
    position: absolute;
    left: 0;
    width: 694px;
    top: 92px;
    margin: 0;
    text-align: center;
    font-weight: 700;
    font-size: 26px;
    letter-spacing: 1px;
    color: var(--brand-red);
    text-transform: uppercase;
  }
  .headline {
    position: absolute;
    left: 0;
    width: 694px;
    top: 196px;
    margin: 0;
    text-align: center;
    font-weight: 500;
    font-size: 44px;
    line-height: 66px;
    letter-spacing: 2px;
    color: var(--text-grey);
    text-transform: uppercase;
  }
  .headline__accent {
    color: var(--brand-red);
  }
</style>
</head>
<body>
  <main class="banner">
    <svg class="banner__shapes" viewBox="0 0 1200 457" xmlns="http://www.w3.org/2000/svg">
      <defs>
        <linearGradient id="mist" x1="0" y1="0" x2="0" y2="1">
          <stop offset="0" stop-color="var(--mist-light)"/>
          <stop offset="0.6" stop-color="var(--mist-dark)"/>
          <stop offset="1" stop-color="var(--mist-light)"/>
        </linearGradient>
        <linearGradient id="photo-tones" x1="0" y1="0" x2="1" y2="1">
          <stop offset="0" stop-color="var(--photo-warm)"/>
          <stop offset="1" stop-color="var(--photo-deep)"/>
        </linearGradient>
      </defs>

      <rect class="backdrop" role="img" aria-label="Faint landscape with a waterfall and misty hills" x="0" y="0" width="700" height="457" fill="url(#mist)" opacity="0.7"/>

      <path class="accent-wave accent-wave--left" fill="var(--brand-red)"
            d="M0 0 L24 0 C52 70 48 190 0 330 Z"/>

      <path class="accent-wave accent-wave--divider" fill="var(--brand-red)"
            d="M640 0 C620 120 680 250 620 340 C592 390 574 430 568 457 L600 457 C606 430 624 390 652 340 C712 250 652 120 672 0 Z"/>

      <path class="photo-area" role="img" aria-label="Photo of a senior barber giving a client a haircut in a classic barber shop"
            fill="url(#photo-tones)"
            d="M660 0 C640 120 700 250 640 340 C612 390 594 430 588 457 L1200 457 L1200 0 Z"/>

      <path class="accent-wave accent-wave--corner" fill="var(--brand-red)"
            d="M1150 0 L1200 0 L1200 95 C1180 70 1162 35 1150 0 Z"/>
    </svg>

    <p class="brand-name">Alpine Counsel</p>

    <h1 class="headline">
      <span class="headline__accent">Clear</span> Guidance<br>
      <span class="headline__accent">No</span> Pitch
    </h1>
  </main>
</body>
</html>
```